Business card for Chiropractic clinics needs reworked / redesigned

The business card in attachment was designed 10 years ago. It is in need of an update.
We have 2 clinics:
HALSPUNT VORDA & HALSPUNT MIRBE
Only one address needs to be on the card for doctors that only work in one clinic and two addresses need to be on the card for the doctors that work in both clinics.

Target Market(s)

patients/referrers

Industry/Entity Type

Medical

Contact Information for Business Card

Logo (in full or zoomed-in)
Clinic Name
Doctor name and title
clinic address, website, tel, email

Font styles to use
Sans Serif

Colors

Designer to choose colors to be used in the design.

Requirements
Must have
• Good contrast/readability
• We like modern minimalistic designs
• The Bcard needs to project our very high standard of proficiency/professionalism
Should not have
• Not curly
• Not to much colours

```html
<!DOCTYPE html>
<html lang="en">
<head>
<meta charset="utf-8">
<title>Halspunt business card</title>
<link rel="stylesheet" href="https://fonts.googleapis.com/css2?family=Montserrat:wght@400;500;700;800&display=swap">
<style>
  :root {
    --teal: #249a93;
    --grey-text: #6a6a6a;
    --grey-line: #7a7a7a;
    --divider: #b9b9b9;
    --paper: #f4f4f4;
    --backdrop: #e6e6e6;
    --white: #ffffff;
  }
  * { margin: 0; padding: 0; box-sizing: border-box; }
  html, body {
    width: 1200px; height: 1185px; overflow: hidden;
    background: var(--backdrop);
    font-family: "Montserrat", Arial, sans-serif;
  }
  .sheet {
    position: relative; width: 1200px; height: 1185px;
    display: flex; flex-direction: column; align-items: center; justify-content: center; gap: 80px;
  }
  .card {
    position: relative; width: 700px; height: 453px; overflow: hidden;
    box-shadow: 0 6px 18px rgba(0,0,0,0.08);
  }
  /* Front */
  .card-front { background: var(--paper); }
  .brand {
    position: absolute; left: 70px; top: 170px;
    display: flex; align-items: center; gap: 12px;
  }
  .brand-name {
    font-weight: 800; font-size: 30px; letter-spacing: 2px; color: var(--grey-text);
    white-space: nowrap;
  }
  .brand-square { width: 11px; height: 11px; background: var(--teal); flex: none; }
  .divider {
    position: absolute; left: 340px; top: 95px; width: 1px; height: 200px;
    background: var(--divider);
  }
  .contact { position: absolute; left: 375px; top: 95px; color: var(--grey-text); }
  .person-name { font-weight: 700; font-size: 21px; letter-spacing: 0.5px; }
  .person-title { font-weight: 500; font-size: 15px; color: var(--teal); margin-top: 2px; }
  .address { font-size: 14px; line-height: 1.4; margin-top: 14px; }
  .details { list-style: none; margin-top: 10px; font-size: 14px; line-height: 1.55; }
  .details li { display: flex; align-items: center; gap: 10px; white-space: nowrap; }
  .details svg { width: 14px; height: 14px; flex: none; }
  .edge-line {
    position: absolute; left: 0; right: 0; bottom: 26px; height: 5px; background: var(--grey-line);
  }
  .edge-band {
    position: absolute; left: 0; right: 0; bottom: 0; height: 20px; background: var(--teal);
  }
  /* Back */
  .card-back { background: var(--teal); }
  .back-brand {
    position: absolute; inset: 0;
    display: flex; align-items: center; justify-content: center; gap: 18px;
  }
  .back-brand .brand-name { color: var(--white); font-size: 52px; letter-spacing: 4px; }
  .back-brand .brand-square { width: 16px; height: 16px; background: var(--white); }
</style>
</head>
<body>
<main class="sheet">
  <section class="card card-front" aria-label="Business card front">
    <div class="brand">
      <span class="brand-square"></span>
      <span class="brand-name">HALSPUNT</span>
    </div>
    <div class="divider"></div>
    <div class="contact">
      <p class="person-name">Marc VERLINDE</p>
      <p class="person-title">Chiropractor</p>
      <p class="address">Lindenlaan 48<br>4710 Vorda</p>
      <ul class="details">
        <li>
          <svg viewBox="0 0 16 16" aria-hidden="true"><path d="M4 1.5 6.2 4 5 5.6c.8 1.9 2.4 3.5 4.4 4.4L11 8.8l2.5 2.2-1.3 2.3C7 13 3 9 2.7 3.8Z" fill="none" stroke="#249a93" stroke-width="1.4" stroke-linejoin="round"/></svg>
          +00 (0)12 345 67 8
        </li>
        <li>
          <svg viewBox="0 0 16 16" aria-hidden="true"><rect x="1.5" y="3.5" width="13" height="9" fill="none" stroke="#249a93" stroke-width="1.3"/><path d="M1.5 3.5 8 9l6.5-5.5" fill="none" stroke="#249a93" stroke-width="1.3"/></svg>
          marc@halspuntvorda.be
        </li>
        <li>
          <svg viewBox="0 0 16 16" aria-hidden="true"><circle cx="8" cy="8" r="6.3" fill="none" stroke="#249a93" stroke-width="1.3"/><ellipse cx="8" cy="8" rx="2.8" ry="6.3" fill="none" stroke="#249a93" stroke-width="1.1"/><path d="M1.7 8h12.6M2.8 4.8h10.4M2.8 11.2h10.4" stroke="#249a93" stroke-width="1.1"/></svg>
          www.halspuntvorda.be
        </li>
      </ul>
    </div>
    <div class="edge-line"></div>
    <div class="edge-band"></div>
  </section>

  <section class="card card-back" aria-label="Business card back">
    <div class="back-brand">
      <span class="brand-square"></span>
      <span class="brand-name">HALSPUNT</span>
    </div>
  </section>
</main>
</body>
</html>
```